IT services company needs a business card designed

-2 sided business card.-Front is going to be the logo raised (3D floating effect) on a black background. Make the logos spider web shiny silver and keep the spider the same design. -Back needs to have the following information:Darrel Sotho, Managing Partner, Cell: 738-402-1954, Website: Plankhorn.com, Email: Darrel@Plankhorn.com
Target Market(s)
IT Services
Industry/Entity Type
It Company
Contact Information for Business Card
-2 sided business card.
-Front is going to be the logo raised (3D floating effect) on a black background. Make the logos spider web shiny silver and keep the spider the same design.
-Back needs to have the following information:
Darrel Sotho, Managing Partner, Cell: 738-402-1954, Website: Plankhorn.com, Email: Darrel@Plankhorn.com

```html
<!DOCTYPE html>
<html lang="en">
<head>
<meta charset="utf-8">
<title>Plankhorn Business Card</title>
<link rel="stylesheet" href="https://fonts.googleapis.com/css2?family=Exo+2:wght@400;500;600&display=swap">
<style>
  :root {
    --stage: #e9eaec;
    --card-dark: #0b0f17;
    --card-light: #ffffff;
    --ink: #111418;
    --silver: #c9ccd1;
    --accent: #1e9ad6;
  }
  * { box-sizing: border-box; margin: 0; padding: 0; }
  html, body { width: 1200px; height: 1189px; overflow: hidden; }
  body {
    background: var(--stage);
    font-family: "Exo 2", sans-serif;
    display: flex;
    flex-direction: column;
    align-items: center;
    justify-content: center;
    gap: 30px;
  }
  .card {
    position: relative;
    width: 960px;
    height: 549px;
    border-radius: 34px;
    overflow: hidden;
    box-shadow: 0 10px 28px rgba(0,0,0,0.18);
  }
  .card--front {
    background: var(--card-dark);
    display: flex;
    flex-direction: column;
    align-items: center;
    justify-content: center;
    gap: 34px;
  }
  .brand-dot {
    width: 150px;
    height: 150px;
    border-radius: 50%;
    background: var(--accent);
  }
  .card--front .brand-name {
    font-size: 76px;
    font-weight: 500;
    letter-spacing: 4px;
    line-height: 1;
    color: var(--silver);
  }
  .card--back { background: var(--card-light); }
  .back-logo {
    position: absolute;
    right: 70px;
    top: 50px;
    display: flex;
    flex-direction: column;
    align-items: center;
    gap: 24px;
  }
  .back-logo .brand-dot { width: 130px; height: 130px; }
  .back-logo .brand-name {
    font-size: 58px;
    font-weight: 500;
    letter-spacing: 3px;
    line-height: 1;
    color: var(--ink);
  }
  .person {
    position: absolute;
    left: 60px;
    top: 300px;
  }
  .person-name {
    font-size: 34px;
    font-weight: 500;
    letter-spacing: 1px;
    color: var(--ink);
    text-transform: uppercase;
    line-height: 1.1;
  }
  .person-role {
    font-size: 29px;
    font-weight: 500;
    color: var(--accent);
    line-height: 1.1;
  }
  .divider {
    position: absolute;
    left: 60px;
    right: 70px;
    top: 384px;
    height: 2px;
    background: var(--accent);
  }
  .website {
    position: absolute;
    right: 70px;
    top: 400px;
    font-size: 28px;
    font-weight: 500;
    line-height: 1.2;
    color: var(--accent);
  }
  .contact-list {
    position: absolute;
    left: 60px;
    top: 408px;
    list-style: none;
    display: flex;
    flex-direction: column;
    gap: 16px;
  }
  .contact-item {
    display: flex;
    align-items: center;
    gap: 18px;
    font-size: 28px;
    line-height: 1.2;
    color: var(--ink);
  }
  .contact-icon { width: 36px; height: 36px; flex: none; }
</style>
</head>
<body>
  <section class="card card--front" aria-label="Card front">
    <div class="brand-dot" aria-hidden="true"></div>
    <div class="brand-name">PLANKHORN</div>
  </section>

  <section class="card card--back" aria-label="Card back">
    <div class="back-logo">
      <div class="brand-dot" aria-hidden="true"></div>
      <div class="brand-name">PLANKHORN</div>
    </div>

    <div class="person">
      <p class="person-name">Darrel Sotho</p>
      <p class="person-role">Managing Partner</p>
    </div>

    <div class="divider"></div>
    <div class="website">Plankhorn.com</div>

    <ul class="contact-list">
      <li class="contact-item">
        <svg class="contact-icon" viewBox="0 0 36 36" aria-hidden="true">
          <circle cx="18" cy="18" r="18" fill="var(--accent)"/>
          <rect x="12" y="9" width="12" height="18" rx="2" fill="none" stroke="#fff" stroke-width="2.2"/>
          <circle cx="18" cy="23.5" r="1.2" fill="#fff"/>
        </svg>
        <span>738-402-1954</span>
      </li>
      <li class="contact-item">
        <svg class="contact-icon" viewBox="0 0 36 36" aria-hidden="true">
          <circle cx="18" cy="18" r="18" fill="var(--accent)"/>
          <rect x="9" y="12" width="18" height="12" rx="1.5" fill="none" stroke="#fff" stroke-width="2"/>
          <path d="M9.5 12.8 L18 19.5 L26.5 12.8" fill="none" stroke="#fff" stroke-width="2"/>
        </svg>
        <span>Darrel@Plankhorn.com</span>
      </li>
    </ul>
  </section>
</body>
</html>
```